hotel's Website

Hotels website redesign for reference pictures, logo etc see http://restwellmarlow.co.uk/

1. 2-3 Special offers on the main page.
2. Booking calender
3. Location Map
4. Picture gallery.
5. Journeyscope reviews.
6. short description
7. Social Media sharing.
8 Phone number and address.

Industry/Entity Type

Hotel

Requirements
Must have
• 1. 2-3 Special offers on the main page.
2. Booking calender
3. Location Map
4. Picture gallery.
5. Journeyscope reviews.
6. short description
7. Social Media sharing.

```html
<!DOCTYPE html>
<html lang="en">
<head>
<meta charset="utf-8">
<title>Restwell Inn London Victoria</title>
<link href="https://fonts.googleapis.com/css2?family=Open+Sans:wght@400;600&family=Arimo:wght@400&display=swap" rel="stylesheet">
<style>
:root{
  --red:#c1272d;
  --orange:#e8502a;
  --ink:#2b2b2b;
  --grey:#8a8a8a;
  --line:#dedede;
  --footer:#3a3a3a;
  --canvas:#ececec;
  --white:#ffffff;
}
*{box-sizing:border-box;margin:0;padding:0}
html,body{width:832px;height:1200px;overflow:hidden}
body{background:var(--canvas);font-family:"Open Sans",sans-serif;color:var(--ink);position:relative}
.page{position:absolute;left:69px;top:16px;width:694px;height:1184px;background:var(--white);box-shadow:0 0 4px rgba(0,0,0,.12)}
.abs{position:absolute}
/* header */
.brand{left:35px;top:8px;display:flex;align-items:center;gap:6px}
.brand-mark{width:14px;height:14px;border-radius:50%;background:var(--orange)}
.brand-name{font-size:14px;font-weight:600;color:var(--red)}
.brand-sub{left:35px;top:62px;font-size:5px;letter-spacing:2px;color:var(--ink);text-transform:uppercase;font-weight:600}
.brand-rule{left:102px;top:11px;width:2px;height:42px;background:var(--orange)}
.location{left:117px;top:28px;font-size:9px;color:var(--orange)}
.call{left:557px;top:14px;font-size:9px;color:var(--grey);display:flex;align-items:center;gap:3px}
.call b{font-weight:400;color:var(--ink)}
.social{left:559px;top:33px;display:flex;gap:2px}
.social span{width:21px;height:22px;background:var(--orange);display:block}
/* nav */
.nav{left:26px;top:70px;width:651px;height:22px;border-bottom:1px solid var(--line);border-top:1px solid #f1f1f1}
.nav a{position:absolute;top:0;height:22px;line-height:22px;font-size:7.5px;color:var(--ink);text-decoration:none;text-transform:uppercase}
.nav a.active{background:var(--red);color:var(--white);text-align:center}
.nav .search{position:absolute;left:529px;top:5px;width:93px;height:13px;border:1px solid #cfcfcf;box-shadow:inset 0 1px 2px rgba(0,0,0,.12)}
.nav .search-icon{position:absolute;left:636px;top:4px}
/* hero */
.hero{left:22px;top:108px;width:651px;height:276px;background:
  radial-gradient(ellipse 40% 50% at 50% 50%,rgba(255,120,30,.55),transparent 70%),
  radial-gradient(ellipse 60% 30% at 50% 95%,rgba(255,150,60,.45),transparent 70%),
  linear-gradient(180deg,#0c1430 0%,#1a2a5a 55%,#2a1a24 100%)}
.hero-caption{left:22px;top:302px;width:210px;height:80px;background:rgba(168,54,24,.85);padding:2px 13px}
.hero-caption h1{font-size:23px;line-height:27px;font-weight:600;color:var(--white);text-transform:uppercase}
/* booking */
.book-title{left:65px;top:430px;font-size:16px;color:var(--orange)}
.book-label{top:422px;font-size:9px;color:var(--ink)}
.hatch{top:431px;width:7px;height:19px;background:repeating-linear-gradient(135deg,#bbb 0 1px,#eee 1px 3px)}
.field{top:431px;height:19px;border:1px solid #d5d5d5;background:var(--white);font-family:Arimo,sans-serif;font-size:8px;color:var(--grey);padding:5px 3px 0}
.field.avail{font-family:"Open Sans",sans-serif;color:var(--ink);padding-top:5px}
.field-btn{left:615px;top:431px;width:19px;height:19px;background:#ececec;border:1px solid #d5d5d5;display:flex;align-items:center;justify-content:center}
.divider{left:21px;top:484px;width:628px;height:1px;background:linear-gradient(90deg,transparent,#d0d0d0 20%,#d0d0d0 80%,transparent)}
/* features */
.feature-dot{top:512px;width:36px;height:36px;border-radius:50%;background:radial-gradient(circle at 50% 35%,#f7c21c,#e8502a 70%,#c1272d)}
.feature h2{position:absolute;top:522px;font-size:15px;font-weight:600;color:var(--ink);text-transform:uppercase;white-space:nowrap}
.feature p{position:absolute;top:556px;width:195px;font-family:Arimo,sans-serif;font-size:8.8px;line-height:14px;color:var(--grey)}
.frame{top:624px;width:208px;height:138px;border:1px solid #eee;box-shadow:0 0 3px rgba(0,0,0,.1);background:var(--white)}
.frame div{position:absolute;left:8px;top:8px;width:192px;height:121px}
.rule{left:21px;top:833px;width:652px;height:1px;background:var(--line)}
/* footer */
.footer{left:0;top:890px;width:694px;height:294px;background:var(--footer)}
.footer h3{position:absolute;font-size:12px;font-weight:400;color:var(--white)}
.arrows{left:148px;top:23px;display:flex;align-items:center;gap:6px}
.arrows .next{width:13px;height:13px;background:var(--red);display:flex;align-items:center;justify-content:center}
.quote{left:21px;top:43px;width:151px;height:136px;background:var(--white);border:1px solid var(--red);padding:18px 12px 0 13px;font-family:Arimo,sans-serif;font-size:8.4px;line-height:14px;color:#666}
.quote-tail{left:52px;top:178px}
.author{left:79px;top:203px;font-family:Arimo,sans-serif;font-size:8px;color:#aaa}
.author span{color:var(--red)}
.tweets{left:269px;top:46px;width:155px;font-family:Arimo,sans-serif;font-size:8.4px;line-height:14px;color:#8a8a8a}
.news-dot{left:473px;top:25px;width:35px;height:35px;border-radius:50%;background:radial-gradient(circle at 50% 35%,#f7c21c,#e8502a 70%,#c1272d)}
.news-input{left:518px;top:27px;width:113px;height:29px;background:var(--white);font-size:7px;color:#777;padding:11px 4px 0;text-transform:uppercase}
.news-btn{left:631px;top:27px;width:38px;height:29px;background:var(--red);display:flex;align-items:center;justify-content:center}
.review-badge{left:505px;top:95px;display:flex;flex-direction:column;align-items:center;gap:6px}
.review-badge i{width:56px;height:56px;border-radius:50%;background:#444;display:block}
.review-badge span{font-size:30px;color:#444;font-weight:400}
.foot-rule{left:21px;top:225px;width:651px;height:1px;background:#4d4d4d}
.copy{left:21px;top:242px;font-family:Arimo,sans-serif;font-size:7.5px;color:#bdbdbd}
</style>
</head>
<body>
<div class="page">
  <header>
    <div class="abs brand"><span class="brand-mark"></span><span class="brand-name">Restwell Inn</span></div>
    <div class="abs brand-sub">by Harbourline Hotels</div>
    <div class="abs brand-rule"></div>
    <div class="abs location">LONDON - VICTORIA</div>
    <div class="abs call">
      <svg width="9" height="8" viewBox="0 0 10 8"><path d="M1 3 Q5 -1 9 3 L8 4 L6.5 3 V2 Q5 1.5 3.5 2 V3 L2 4 Z M3 4 H7 L8 7 H2 Z" fill="#2b2b2b"/></svg>
      Call Us : <b>+00 123456789</b>
    </div>
    <div class="abs social" aria-label="Social media links">
      <span></span><span></span><span></span><span></span><span></span>
    </div>
    <nav class="abs nav">
      <a class="active" style="left:0;width:50px">Home</a>
      <a style="left:65px">Our Rooms</a>
      <a class="active" style="left:124px;width:53px">Attractions</a>
      <a style="left:182px">London Events</a>
      <a style="left:250px">Special Offers</a>
      <a style="left:319px">Photos</a>
      <a style="left:358px">Directions</a>
      <a style="left:412px">Contact</a>
      <span class="search"></span>
      <svg class="search-icon" width="12" height="12" viewBox="0 0 12 12"><circle cx="5" cy="5" r="3.8" fill="none" stroke="#2b2b2b" stroke-width="1.6"/><path d="M7.8 7.8 L11 11" stroke="#2b2b2b" stroke-width="1.8"/></svg>
    </nav>
  </header>

  <section>
    <div class="abs hero" role="img" aria-label="Giant observation wheel lit orange at night with searchlight beams over the river"></div>
    <div class="abs hero-caption"><h1>Visit London<br>Cult and<br>Culture</h1></div>
  </section>

  <section class="booking">
    <div class="abs book-title">BOOK A ROOM</div>
    <div class="abs book-label" style="left:186px">FROM</div>
    <div class="abs book-label" style="left:340px">TO</div>
    <span class="abs hatch" style="left:179px"></span>
    <div class="abs field" style="left:186px;width:141px">Input your text here</div>
    <span class="abs hatch" style="left:328px"></span>
    <div class="abs field" style="left:338px;width:141px"></div>
    <span class="abs hatch" style="left:480px"></span>
    <div class="abs field avail" style="left:491px;width:124px">SEARCH AVAILABILITY</div>
    <div class="abs field-btn"><svg width="9" height="9" viewBox="0 0 12 12"><circle cx="5" cy="5" r="3.8" fill="none" stroke="#888" stroke-width="1.4"/><path d="M7.8 7.8 L11 11" stroke="#888" stroke-width="1.6"/></svg></div>
    <span class="abs hatch" style="left:634px"></span>
    <div class="abs divider"></div>
  </section>

  <section class="features">
    <div class="feature">
      <span class="abs feature-dot" style="left:19px"></span>
      <h2 style="left:67px">Special Offers</h2>
      <p style="left:21px">Lorem ipsum dolor consectetur adipscing elit. Ut accumsan eros eget est venenatis sit amet mattis arc interdum. Nulla pretium lacus in turpis dapus non mollis elit mollis.</p>
    </div>
    <div class="feature">
      <span class="abs feature-dot" style="left:239px"></span>
      <h2 style="left:285px">Explore London</h2>
      <p style="left:243px">Lorem ipsum dolor consectetur adipscing elit. Ut accumsan eros eget est venenatis sit amet mattis arc interdum. Nulla pretium lacus in turpis dapus non mollis elit mollis.</p>
    </div>
    <div class="feature">
      <span class="abs feature-dot" style="left:458px"></span>
      <h2 style="left:499px">Stay in Confort</h2>
      <p style="left:465px">Lorem ipsum dolor consectetur adipscing elit. Ut accumsan eros eget est venenatis sit amet mattis arc interdum. Nulla pretium lacus in turpis dapus non mollis elit mollis.</p>
    </div>
    <div class="abs frame" style="left:26px"><div role="img" aria-label="Red double-decker buses on a black and white city street" style="background:linear-gradient(90deg,#6b6b6b,#b8b8b8 30%,#c1272d 45%,#a42226 75%,#8a8a8a)"></div></div>
    <div class="abs frame" style="left:246px"><div role="img" aria-label="Red London guidebook beside a street map" style="background:linear-gradient(90deg,#c8151b 0 50%,#2a2a2a 50% 52%,#d8d3b8 52%,#c9d6c0)"></div></div>
    <div class="abs frame" style="left:464px"><div role="img" aria-label="Hotel room with white sofa, red cushions and striped wall" style="background:linear-gradient(180deg,#c9c4c0,#e6e2de 55%,#b8262a 85%,#d9d5d0)"></div></div>
    <div class="abs rule"></div>
  </section>

  <footer class="abs footer">
    <h3 style="left:20px;top:20px">What Client’s Say</h3>
    <div class="abs arrows">
      <svg width="6" height="8" viewBox="0 0 6 8"><path d="M5 1 L2 4 L5 7" fill="none" stroke="#fff" stroke-width="1.2"/></svg>
      <span class="next"><svg width="6" height="8" viewBox="0 0 6 8"><path d="M1 1 L4 4 L1 7" fill="none" stroke="#fff" stroke-width="1.2"/></svg></span>
    </div>
    <div class="abs quote">Lorem ipsum consecetur adipisc-ing donec nunc ipsum, loboris convallis laoret enim. Aliquam hendrerit rutrum iaculis. Aliquam vitae odio elit. Nullam ondimen-tum etiam maluada velit beum donec sit amet augue tristique.</div>
    <svg class="abs quote-tail" width="22" height="20" viewBox="0 0 22 20"><path d="M0 0 L20 20 V0 Z" fill="#fff"/><path d="M0 0 L20 20 V0" fill="none" stroke="#c1272d"/></svg>
    <div class="abs author"><span>Marta Velli</span>, Manager</div>

    <h3 style="left:269px;top:20px;font-size:10px;font-weight:600">Latest Tweets</h3>
    <p class="abs tweets">Lorem ipsum dolor consectetur adipsc-ing elit. Ut accumsan eros eget est venenatis sit amet mattis arc interdum. Nulla pretium lacus in turpis dapus non mollis elit mollis.</p>

    <span class="abs news-dot"></span>
    <div class="abs news-input">Join our newsletter</div>
    <div class="abs news-btn"><svg width="6" height="8" viewBox="0 0 6 8"><path d="M1 1 L4 4 L1 7" fill="none" stroke="#fff" stroke-width="1.2"/></svg></div>
    <div class="abs review-badge" aria-label="Journeyscope reviews"><i></i><span>Journeyscope</span></div>

    <div class="abs foot-rule"></div>
    <div class="abs copy">Copyright © 2013 all rights reserved</div>
  </footer>
</div>
</body>
</html>
```